Create lumora book cover: Step Aside

I need a cover designed for my book
Title is “Step Aside”
Tag line is “ The Venture Horizon Plan“

With the words “ A handbook on how to remove yourself from your company“ somewhere on the page.

Author name “Neil Corbett”

The cover will be used on lumora and paper back and needs to comply with all RVS formatting rules.

Target Market(s)

Small Business owners

Font styles to use
Serif

```html
<!DOCTYPE html>
<html lang="en">
<head>
<meta charset="utf-8">
<title>Step Aside – Book Cover</title>
<link rel="stylesheet" href="https://fonts.googleapis.com/css2?family=Anton&family=Oswald:wght@500;600&family=Poppins:wght@700&display=swap">
<style>
  :root {
    --navy: #1c2566;
    --navy-light: #2a3a8c;
    --navy-deep: #141a52;
    --yellow: #fde01a;
    --red: #d8252c;
    --grey: #a5a7ab;
    --white: #ffffff;
    --backdrop: #e4e4e4;
  }
  * { margin: 0; padding: 0; box-sizing: border-box; }
  html, body {
    width: 1200px;
    height: 1200px;
    overflow: hidden;
    background: var(--backdrop);
  }
  .canvas {
    position: relative;
    width: 1200px;
    height: 1200px;
  }
  .book-cover {
    position: absolute;
    left: 220px;
    top: 50px;
    width: 760px;
    height: 1100px;
    display: block;
    box-shadow: 0 10px 30px rgba(0,0,0,0.18);
  }
  .title-main { font-family: "Anton", "Oswald", sans-serif; fill: var(--navy-deep); }
  .title-accent { font-family: "Anton", "Oswald", sans-serif; fill: var(--red); }
  .subtitle { font-family: "Poppins", sans-serif; font-weight: 700; fill: var(--white); }
  .tagline { font-family: "Oswald", sans-serif; font-weight: 500; fill: var(--navy-deep); }
  .author { font-family: "Oswald", sans-serif; font-weight: 600; fill: var(--white); }
</style>
</head>
<body>
<main class="canvas">
  <svg class="book-cover" viewBox="0 0 760 1100" xmlns="http://www.w3.org/2000/svg" aria-label="Step Aside by Neil Corbett – book cover">
    <defs>
      <radialGradient id="navy-glow" cx="0.5" cy="0.45" r="0.6">
        <stop offset="0" stop-color="var(--navy-light)"/>
        <stop offset="1" stop-color="var(--navy)"/>
      </radialGradient>
      <clipPath id="cover-clip"><rect width="760" height="1100"/></clipPath>
    </defs>

    <g clip-path="url(#cover-clip)">
      <rect class="band-navy" width="760" height="1100" fill="url(#navy-glow)"/>
      <polygon class="band-yellow" points="0,135 520,0 760,0 760,350 0,497" fill="var(--yellow)"/>
      <polygon class="band-grey" points="0,845 760,700 760,1100 0,1100" fill="var(--grey)"/>

      <g class="title-block" transform="rotate(-12 380 550)">
        <text class="title-main" x="60" y="410" font-size="380" textLength="640" lengthAdjust="spacingAndGlyphs">STEP</text>
        <text class="title-accent" x="70" y="640" font-size="230" textLength="600" lengthAdjust="spacingAndGlyphs">ASIDE</text>
        <text class="subtitle" x="75" y="720" font-size="40">The Venture Horizon Plan</text>
        <text class="tagline" x="40" y="800" font-size="24" textLength="650" lengthAdjust="spacingAndGlyphs">A handbook on how to remove yourself from your company</text>
        <text class="author" x="300" y="885" font-size="54">Neil Corbett</text>
      </g>
    </g>
  </svg>
</main>
</body>
</html>
```